Home Page Design

Please see design brief attached. Concept here: sketchboard[dot]io/file/qWm83LzpR7cvXuNtYa2KhE/Brindlemoor---Landing-Page?node-id=0%3A1&t=PKr92mvnQsD4xTcZ-1

Industry/Entity Type

Wedding

Number of Pages Required

1 page

Font styles to use
Serif
Sans Serif
Decorative
Script

Colors
A7469A
B969AE
D3A5CF
EDDBEB
F8F0F9
6B429C
8869AF
B7A5CE
E3DAEB
F3F0F8

Requirements
Must have
• Please see attached PDF
Nice to have
• Please see attached PDF
Should not have
• Please see attached PDF

```html
<!DOCTYPE html>
<html lang="en">
<head>
<meta charset="utf-8">
<title>Brindlemoor – Home</title>
<link rel="stylesheet" href="https://fonts.googleapis.com/css2?family=Marcellus&family=Lato:wght@400;700&display=swap">
<style>
:root{
  --plum:#6B429C;
  --violet:#8869AF;
  --lilac:#B7A5CE;
  --mist:#E3DAEB;
  --haze:#F3F0F8;
  --rose:#D3A5CF;
  --blush:#EDDBEB;
  --ink:#3b3346;
  --grey:#8a8494;
  --white:#ffffff;
  --forest:#1f3330;
}
*{box-sizing:border-box;margin:0;padding:0}
html,body{width:1200px;height:1200px;overflow:hidden;background:var(--white)}
.stage{position:absolute;left:0;top:0;width:1920px;height:1920px;transform:scale(.625);transform-origin:0 0;font-family:"Lato",sans-serif;color:var(--ink)}
.abs{position:absolute}
.serif{font-family:"Marcellus",serif}
.photo{position:absolute}

/* hero */
.hero{left:825px;top:134px;width:282px;height:124px;background:linear-gradient(100deg,#17302b 0%,#24403a 45%,#3a4a3c 62%,#1c2f2a 100%)}
.brand{left:846px;top:158px;width:48px;text-align:center;color:var(--white);font-family:"Marcellus",serif;font-size:6px}
.brand small{display:block;font-family:"Lato",sans-serif;font-size:1.6px;opacity:.8;margin-top:1px}
.brand .dot{display:block;width:4px;height:4px;border-radius:50%;background:var(--white);margin:0 auto 1px}
.nav-btn{top:158px;height:6px;border:.4px solid var(--white);color:var(--white);font-size:2px;line-height:5.2px;text-align:center}
.hero-title{left:848px;top:198px;color:var(--white);font-family:"Marcellus",serif;font-size:9.5px;line-height:10.5px}
.ghost-btn{height:8px;border:.5px solid currentColor;font-size:2.2px;line-height:7px;text-align:center}

/* stats */
.stats{left:825px;top:258px;width:282px;height:55px;background:var(--violet)}
.stat{top:280px;color:var(--white);display:flex;align-items:center;gap:3px}
.stat b{font-family:"Marcellus",serif;font-weight:400;font-size:6.5px;display:block;line-height:6px}
.stat span{font-size:2px;opacity:.85}

/* intro */
.frame{left:855px;top:336px;width:102px;height:116px;background:var(--white);box-shadow:0 1px 4px rgba(107,66,156,.25);padding:3px}
.frame .photo{position:relative;width:100%;height:100%;background:linear-gradient(160deg,#6d6258,#b8aca0 50%,#4a3f3a)}
.flower{background:radial-gradient(circle at 50% 50%,#f4dde6 0%,#f7eaf0 45%,rgba(255,255,255,0) 72%)}
.h2{font-family:"Marcellus",serif;font-size:7.4px;line-height:8.6px;color:var(--ink)}
.tiny{font-size:2px;line-height:2.6px;color:var(--grey)}

/* testimonials */
.fade{background:var(--blush);opacity:.35}
.quote{top:515px;width:73px;height:64px;background:var(--white);box-shadow:0 1px 4px rgba(0,0,0,.12);padding:6px 7px}
.quote p{font-size:1.9px;line-height:2.8px;color:var(--grey)}
.quote .who{position:absolute;left:7px;bottom:8px;display:flex;gap:3px;align-items:center}
.avatar{width:6px;height:6px;border-radius:50%;background:linear-gradient(135deg,#7a6050,#c9b3a3)}
.stars{color:var(--violet);font-size:2.6px;letter-spacing:.3px}
.arrow{top:547px;width:6px;height:6px;color:var(--violet)}

/* how it works */
.step{top:655px;width:72px;height:85px;background:var(--violet);color:var(--white);text-align:center;padding:9px 5px 0}
.step .icon{width:14px;height:14px;border-radius:50%;background:var(--white);margin:0 auto 4px;display:flex;align-items:center;justify-content:center}
.step h4{font-weight:400;font-size:2.8px;line-height:3.4px;margin-bottom:2px}
.step p{font-size:1.8px;line-height:2.6px;opacity:.85}
.insured{left:854px;top:743px;width:224px;height:51px;background:var(--violet);color:var(--white);padding:10px 8px 0 40px}
.insured .icon{position:absolute;left:8px;top:12px;width:26px;height:26px;border-radius:50%;background:var(--white);display:flex;align-items:center;justify-content:center}
.insured h4{font-weight:400;font-size:2.8px;line-height:3.6px}
.insured p{font-size:1.8px;line-height:2.6px;opacity:.85;margin-top:1px}

/* marketplace */
.market{left:825px;top:817px;width:282px;height:544px;background:var(--haze)}
.tab{top:867px;font-size:2.2px;color:var(--grey)}
.tile{position:absolute;width:54px;overflow:hidden}
.tile span{position:absolute;left:5px;bottom:3px;color:var(--white);font-size:2.6px}
.tile::after{content:"";position:absolute;left:0;right:0;bottom:0;height:40%;background:linear-gradient(rgba(0,0,0,0),rgba(0,0,0,.55))}
.tile span{z-index:1}
.c1{left:854px}.c2{left:914px}.c3{left:973px}.c4{left:1032px}
.g-green{background:linear-gradient(160deg,#6b7f62,#3e5140)}
.g-warm{background:linear-gradient(160deg,#cbb9a9,#6e5a4e)}
.g-grey{background:linear-gradient(160deg,#b4b2b4,#4e4b52)}
.g-purple{background:linear-gradient(160deg,#c3a9d9,#7d5aa6)}
.g-blue{background:linear-gradient(160deg,#4d5f84,#262c44)}
.g-teal{background:linear-gradient(160deg,#3fa0ad,#2b7481)}
.g-cream{background:linear-gradient(160deg,#e9e2d7,#9d9284)}
.g-pink{background:linear-gradient(160deg,#e8c3d4,#8d6a7d)}
.g-gold{background:linear-gradient(160deg,#e8c88a,#7b6b4e)}

/* download */
.dl-box{left:935px;top:1421px;width:145px;height:58px;background:var(--violet);color:var(--white);padding:13px 10px}
.dl-box h3{font-family:"Marcellus",serif;font-weight:400;font-size:5.6px;line-height:7.4px}

/* book */
.book-photo{left:850px;top:1528px;width:230px;height:101px;background:linear-gradient(100deg,#4a4039 0%,#8d8075 35%,#d9d0cc 55%,#6e6660 80%,#3c3632 100%)}
.book-copy{left:861px;top:1601px;width:200px;color:var(--white)}

/* footer */
.footer{left:825px;top:1640px;width:282px;height:158px}
.fcol{top:1698px;color:var(--white)}
.fcol h5{font-weight:700;font-size:2.1px;margin-bottom:3px}
.fcol li{list-style:none;font-size:1.8px;line-height:2.9px;opacity:.85}
</style>
</head>
<body>
<div class="stage">

  <!-- Hero -->
  <div class="abs hero photo" role="img" aria-label="Couple embracing in front of an ivy wall"></div>
  <div class="abs brand"><span class="dot"></span>Brindlemoor<small>wedding planning made simple</small></div>
  <div class="abs nav-btn" style="left:1028px;width:15px">Login</div>
  <div class="abs nav-btn" style="left:1046px;width:19px">Register</div>
  <div class="abs nav-btn" style="left:1067px;width:7px;line-height:4px">≡</div>
  <h1 class="abs hero-title" style="font-weight:400">Be the couple<br>who stuck to their budget!</h1>
  <div class="abs ghost-btn" style="left:848px;top:229px;width:30px;color:var(--white)">Get Started</div>

  <!-- Stats -->
  <div class="abs stats"></div>
  <div class="abs stat" style="left:871px">
    <svg width="8" height="9" viewBox="0 0 8 9" fill="none" stroke="#fff" stroke-width=".5"><path d="M4 8.5C1.5 5.5 1 4.5 1 3.3a3 3 0 0 1 6 0C7 4.5 6.5 5.5 4 8.5z"/><circle cx="4" cy="3.3" r="1"/></svg>
    <div><b>700</b><span>Venues</span></div></div>
  <div class="abs stat" style="left:916px">
    <svg width="9" height="9" viewBox="0 0 9 9" fill="none" stroke="#fff" stroke-width=".5"><rect x="1" y="1" width="7" height="7"/><path d="M1 3h7M3 5h1M5 5h1M3 6.5h1M5 6.5h1"/></svg>
    <div><b>1500</b><span>Vendors</span></div></div>
  <div class="abs stat" style="left:962px">
    <svg width="9" height="9" viewBox="0 0 9 9" fill="none" stroke="#fff" stroke-width=".5"><rect x="1" y="1.5" width="7" height="6.5"/><path d="M1 3.5h7M3 1v1.5M6 1v1.5"/></svg>
    <div><b>500</b><span>Wedding Services</span></div></div>
  <div class="abs stat" style="left:1022px">
    <svg width="9" height="9" viewBox="0 0 9 9" fill="none" stroke="#fff" stroke-width=".5"><circle cx="4" cy="4.5" r="3"/><path d="M4 3v3M6.5 6.5l2 2"/></svg>
    <div><b>$7,680</b><span>Average Saved</span></div></div>

  <!-- Intro -->
  <div class="abs flower photo" style="left:1060px;top:312px;width:50px;height:62px" role="img" aria-label="Pink blossom branch decoration"></div>
  <div class="abs flower photo" style="left:820px;top:418px;width:48px;height:72px" role="img" aria-label="Pink blossom branch decoration"></div>
  <div class="abs frame"><div class="photo" role="img" aria-label="Bride and groom walking under falling bubbles"></div></div>
  <h2 class="abs h2" style="left:968px;top:372px;font-weight:400">Because life is too short<br>to wait for vendors to reply</h2>
  <p class="abs tiny" style="left:968px;top:395px">Focus on enjoying your wedding<br>Get quotes and confirm bookings in minutes</p>
  <div class="abs ghost-btn" style="left:968px;top:410px;width:29px;color:var(--plum)">Explore</div>

  <!-- Testimonials -->
  <div class="abs fade photo" style="left:825px;top:494px;width:58px;height:45px" role="img" aria-label="Faded wedding photo"></div>
  <div class="abs fade photo" style="left:896px;top:470px;width:32px;height:36px" role="img" aria-label="Faded wedding photo"></div>
  <div class="abs fade photo" style="left:1000px;top:494px;width:50px;height:22px" role="img" aria-label="Faded wedding photo"></div>
  <div class="abs fade photo" style="left:1060px;top:480px;width:47px;height:28px" role="img" aria-label="Faded wedding photo"></div>
  <div class="abs fade photo" style="left:876px;top:586px;width:40px;height:26px" role="img" aria-label="Faded wedding photo"></div>
  <div class="abs fade photo" style="left:976px;top:586px;width:53px;height:36px" role="img" aria-label="Faded wedding photo"></div>
  <div class="abs fade photo" style="left:1072px;top:560px;width:35px;height:52px" role="img" aria-label="Faded wedding photo"></div>
  <h2 class="abs h2" style="left:900px;top:500px;width:132px;text-align:center;font-weight:400">Our Customer Loves us</h2>

  <div class="abs quote" style="left:855px"><p>Booking our venue and florist took one evening. Prices were clear and every vendor replied fast. We stayed on budget without any stress at all.</p><div class="who"><div class="avatar"></div><div><div class="stars">★★★★★</div><div class="tiny">Client Name</div></div></div></div>
  <div class="abs quote" style="left:933px"><p>Booking our venue and florist took one evening. Prices were clear and every vendor replied fast. We stayed on budget without any stress at all.</p><div class="who"><div class="avatar"></div><div><div class="stars">★★★★★</div><div class="tiny">Client Name</div></div></div></div>
  <div class="abs quote" style="left:1012px"><p>Booking our venue and florist took one evening. Prices were clear and every vendor replied fast. We stayed on budget without any stress at all.</p><div class="who"><div class="avatar"></div><div><div class="stars">★★★★★</div><div class="tiny">Client Name</div></div></div></div>
  <svg class="abs arrow" style="left:832px" viewBox="0 0 6 6"><path d="M4 1L1.5 3 4 5z" fill="currentColor"/></svg>
  <svg class="abs arrow" style="left:1094px" viewBox="0 0 6 6"><path d="M2 1l2.5 2L2 5z" fill="currentColor"/></svg>

  <!-- How it works -->
  <div class="abs flower photo" style="left:1066px;top:628px;width:44px;height:62px" role="img" aria-label="Pink blossom branch decoration"></div>
  <div class="abs flower photo" style="left:820px;top:700px;width:38px;height:72px" role="img" aria-label="Pink blossom branch decoration"></div>
  <h2 class="abs h2" style="left:900px;top:639px;width:132px;text-align:center;font-weight:400">How it Works</h2>

  <div class="abs step" style="left:854px"><div class="icon"><svg width="8" height="8" viewBox="0 0 8 8" fill="none" stroke="#8869AF" stroke-width=".5"><rect x=".5" y="1" width="7" height="6"/><circle cx="5" cy="4.5" r="1.3"/><path d="M1.5 3h2M1.5 4.5h2"/></svg></div><h4>Browse<br>Top Vendors</h4><p>Compare venues, planners and florists side by side with honest reviews, real photos and clear package prices before you reach out.</p></div>
  <div class="abs step" style="left:930px"><div class="icon"><svg width="8" height="8" viewBox="0 0 8 8" fill="none" stroke="#8869AF" stroke-width=".5"><rect x="2.5" y=".5" width="3" height="7" rx=".5"/><path d="M3.5 3h1M3.5 4h1"/></svg></div><h4>Instantly Book with<br>Pre-Negotiated Prices</h4><p>Pick a date and reserve in one step. Every rate is agreed in advance so the price you see is the price you pay.</p></div>
  <div class="abs step" style="left:1006px"><div class="icon"><svg width="8" height="8" viewBox="0 0 8 8" fill="none" stroke="#8869AF" stroke-width=".5"><circle cx="4.5" cy="3" r="2"/><path d="M.5 6h2l2 1 3-1.5"/></svg></div><h4>Pay<br>over time</h4><p>Split the total into simple monthly payments with no hidden fees, and track every balance from one tidy dashboard.</p></div>
  <div class="abs insured"><div class="icon"><svg width="10" height="12" viewBox="0 0 10 12" fill="none" stroke="#8869AF" stroke-width=".6"><path d="M5 1l4 1.5v3.5c0 2.5-2 4.5-4 5-2-.5-4-2.5-4-5V2.5z"/><circle cx="5" cy="6" r="1.5"/></svg></div><h4>Relaxed!<br>Because life happens. All your bookings are fully insured</h4><p>If a vendor cancels or plans change, your deposit is protected and we help you rebook quickly at the same agreed price, so your day stays on track.</p></div>

  <!-- Marketplaces -->
  <div class="abs market"></div>
  <h2 class="abs h2" style="left:880px;top:834px;width:172px;text-align:center;font-weight:400">Explore our Marketplaces</h2>
  <p class="abs tiny" style="left:885px;top:848px;width:162px;text-align:center">Find trusted local and digital wedding services in one place, each with fixed prices, real reviews and instant booking for every part of your day.</p>
  <div class="abs tab" style="left:936px;color:var(--ink);text-decoration:underline">Local Services</div>
  <div class="abs tab" style="left:963px">Digital Services</div>

  <div class="tile c1 g-green" style="top:886px;height:67px" role="img" aria-label="Garden gazebo venue"><span>Venues</span></div>
  <div class="tile c1 g-warm" style="top:960px;height:47px" role="img" aria-label="Bride having hair styled"><span>Hair &amp; Makeup</span></div>
  <div class="tile c1 g-grey" style="top:1014px;height:46px" role="img" aria-label="Officiant at ceremony"><span>Officiants</span></div>
  <div class="tile c1 g-warm" style="top:1069px;height:47px" role="img" aria-label="Couple in wedding attire"><span>Dresses &amp; Attire</span></div>
  <div class="tile c1 g-green" style="top:1123px;height:67px" role="img" aria-label="Hanging glass lights in trees"><span>Decor &amp; Lighting</span></div>
  <div class="tile c1 g-cream" style="top:1196px;height:67px" role="img" aria-label="Bride wearing necklace"><span>Jewellers</span></div>
  <div class="tile c1 g-gold" style="top:1268px;height:67px" role="img" aria-label="Couple dancing outdoors"><span>Dance Lessons</span></div>

  <div class="tile c2 g-grey" style="top:895px;height:66px" role="img" aria-label="Bride portrait"><span>Photographers</span></div>
  <div class="tile c2 g-grey" style="top:968px;height:67px" role="img" aria-label="Guests at reception"><span>Caterers</span></div>
  <div class="tile c2 g-green" style="top:1042px;height:69px" role="img" aria-label="Wedding gown on hanger"><span>Bridal Gowns</span></div>
  <div class="tile c2 g-pink" style="top:1119px;height:65px" role="img" aria-label="Floral wedding cake"><span>Cakes</span></div>
  <div class="tile c2 g-cream" style="top:1190px;height:67px" role="img" aria-label="Wrapped gift boxes"><span>Favours &amp; Gifts</span></div>

  <div class="tile c3 g-purple" style="top:886px;height:47px" role="img" aria-label="DJ mixing desk"><span>DJs</span></div>
  <div class="tile c3 g-purple" style="top:940px;height:66px" role="img" aria-label="Bridesmaids holding bouquets"><span>Florists</span></div>
  <div class="tile c3 g-green" style="top:1014px;height:66px" role="img" aria-label="Guests posing in photo booth"><span>Photobooths</span></div>
  <div class="tile c3 g-blue" style="top:1087px;height:66px" role="img" aria-label="Flower decorated car"><span>Limos / Transportation</span></div>
  <div class="tile c3 g-teal" style="top:1160px;height:67px" role="img" aria-label="Hot air balloons in sky"><span>Travel Agents</span></div>
  <div class="tile c3 g-blue" style="top:1234px;height:67px" role="img" aria-label="Wedding coordinator portrait"><span>Wedding Coordinators</span></div>

  <div class="tile c4 g-cream" style="top:895px;height:66px" role="img" aria-label="Planner fitting a wedding dress"><span>Planners</span></div>
  <div class="tile c4 g-grey" style="top:968px;height:47px" role="img" aria-label="Video camera on set"><span>Videographers</span></div>
  <div class="tile c4 g-green" style="top:1022px;height:47px" role="img" aria-label="Wedding rings"><span>Bands</span></div>
  <div class="tile c4 g-blue" style="top:1076px;height:47px" role="img" aria-label="Ceremony seating area"><span>Rentals /<br>Ceremony Areas</span></div>
  <div class="tile c4 g-warm" style="top:1130px;height:66px" role="img" aria-label="Wedding invitation cards"><span>Wedding Invitations</span></div>
  <div class="tile c4 g-cream" style="top:1203px;height:67px" role="img" aria-label="Gift boxes with flowers"><span>Favours &amp; Gifts</span></div>

  <!-- Download -->
  <div class="abs flower photo" style="left:996px;top:1396px;width:40px;height:30px" role="img" aria-label="Pink blossom decoration"></div>
  <div class="abs flower photo" style="left:1010px;top:1470px;width:74px;height:36px" role="img" aria-label="Pink blossom decoration"></div>
  <div class="abs photo" style="left:850px;top:1391px;width:149px;height:99px;background:linear-gradient(110deg,#e8e3dc,#d8c7b8 50%,#b79f8e)" role="img" aria-label="Wedding planner working in a bright studio"></div>
  <div class="abs dl-box"><h3>Download our free PDF<br>and Start down the road to saving money</h3>
    <div class="ghost-btn" style="margin-top:4px;width:41px">Download PDF</div></div>

  <!-- Book -->
  <p class="abs tiny" style="left:850px;top:1508px;color:var(--ink)">Reclaim your sanity</p>
  <h2 class="abs h2" style="left:850px;top:1514px;font-weight:400">Book today!</h2>
  <div class="abs photo book-photo" role="img" aria-label="Couple holding a bouquet in an old courtyard"></div>
  <div class="abs book-copy"><div style="font-family:Marcellus,serif;font-size:3px">ACCEPT THE THINGS YOU CAN NOT CHANGE</div>
    <p style="font-size:1.8px;line-height:2.6px;opacity:.85;margin-top:1px">Some details will shift along the way, and that is fine. Lock in the vendors you love early, keep a little room in the budget and let the rest unfold on the day.</p></div>

  <!-- Footer -->
  <svg class="abs footer" viewBox="0 0 282 158" preserveAspectRatio="none"><path d="M0 14Q140 8 282 0V158H0z" fill="#8869AF"/></svg>
  <div class="abs brand" style="left:942px;top:1668px"><span class="dot"></span>Brindlemoor<small>wedding planning made simple</small></div>
  <div class="abs fcol" style="left:843px"><h5>Local Service</h5><ul><li>Photographers</li><li>DJs</li><li>Hair &amp; Makeup</li><li>Planners</li><li>Caterers</li><li>Florists</li><li>Videographers</li><li>Officiants</li><li>Rentals</li><li>Photobooths</li><li>Bands</li></ul></div>
  <div class="abs fcol" style="left:885px"><h5>&nbsp;</h5><ul><li>Dresses &amp; Attire</li><li>Cakes</li><li>Limos / Transportation</li><li>Ceremony Areas</li><li>Decor &amp; Lighting</li><li>Invitations</li><li>Travel Agents</li><li>Jewellers</li><li>Favours &amp; Gifts</li><li>Wedding Coordinators</li><li>Dance Lessons</li></ul></div>
  <div class="abs fcol" style="left:941px"><h5>Digital Services</h5><ul><li>Logo Design</li><li>Website Builders</li><li>Videography</li><li>Invitation Design</li><li>Image Editing</li><li>Guest List Tools</li><li>Speechwriting</li><li>Seating Chart Tools</li></ul></div>
  <div class="abs fcol" style="left:992px"><h5>Vendors</h5><ul><li>How it works</li><li>List a Service</li><li>Vendor Guidelines</li><li>Become a Partner</li></ul></div>
  <div class="abs fcol" style="left:1043px"><h5>Have you Done Planning?</h5><ul><li>About Brindlemoor</li><li>Contact</li><li>Careers</li><li>Press &amp; News</li><li>Terms of Use</li><li>Privacy Policy</li><li>Help Centre</li></ul></div>
  <div class="abs" style="left:925px;top:1788px;width:82px;text-align:center;color:var(--white);font-size:1.8px;opacity:.85">© Brindlemoor 2023</div>

</div>
</body>
</html>
```